Winery label for Birchfall Ridge Winery

New Winery on 265 acre farm in West Central Indiana, presently 10 acres of vineyard increasing to 16 acres in spring of 2018. An Estate Winery as wine will be produced from vine to bottle onsite. An event profit center is planned. Beautiful property with abundant wildlife including a large population of American Eagles , waterfowl, upland game, Marrow Fen Canal system traverses the property , abundant Native American artifacts on site , property bordered by Pell Run and its mouth at the Dunmoor River. Entered the Tolvane Open Vintners Trial in July 2016 as an amateur and won three medals for BRW Wine.
Updates
I am changing my BIRCHFALL RIDGE WINERY with the deer. It has a potential copywriter infringement. How can I send a jpeg pic to all designers ? .
Target Market(s)
100 mile radius, upscale easily recognized brand-label-logo, onsite sale, events,wine club distribution
Industry/Entity Type
Farm
Colors
Designer to choose colors to be used in the design.
Requirements
Must have
- eye appeal and brand recognition
Nice to have
- Read project description
Should not have
- Brand rights conflicts

```html
<!DOCTYPE html>
<html lang="en">
<head>
<meta charset="utf-8">
<title>Birchfall Ridge Estate Winery – Chardonay Label</title>
<link href="https://fonts.googleapis.com/css2?family=Macondo&family=Pinyon+Script&display=swap" rel="stylesheet">
<style>
  :root {
    --page: #ffffff;
    --label-green: #1c4a2b;
    --label-green-dark: #0f3019;
    --label-green-light: #2b5c38;
    --title-fill: #f2bf93;
    --title-edge: #6f7f97;
    --varietal: #f0a245;
    --scene-sky: #a9b4c4;
    --scene-trees: #8a5a2e;
    --scene-bank: #2e3a22;
    --scene-water: #9aa3ab;
  }
  html, body {
    margin: 0;
    padding: 0;
    width: 1052px;
    height: 1200px;
    overflow: hidden;
    background: var(--page);
  }
  .label {
    position: absolute;
    left: 158px;
    top: 111px;
    width: 634px;
    height: 985px;
    overflow: hidden;
    background:
      radial-gradient(ellipse at 30% 20%, var(--label-green-light) 0%, transparent 55%),
      radial-gradient(ellipse at 75% 70%, var(--label-green-light) 0%, transparent 50%),
      radial-gradient(ellipse at 85% 15%, var(--label-green-dark) 0%, transparent 45%),
      radial-gradient(ellipse at 15% 85%, var(--label-green-dark) 0%, transparent 45%),
      var(--label-green);
  }
  .winery-name {
    position: absolute;
    left: 0;
    right: 0;
    top: 36px;
    margin: 0;
    text-align: center;
    white-space: nowrap;
    font-family: "Macondo", cursive;
    font-weight: 400;
    font-size: 90px;
    line-height: 96px;
    color: var(--title-fill);
    -webkit-text-stroke: 1.5px var(--title-edge);
    text-shadow: 2px 3px 2px rgba(70, 85, 110, 0.9);
  }
  .estate-scene {
    position: absolute;
    left: 137px;
    top: 254px;
    width: 373px;
    height: 552px;
    background: linear-gradient(180deg,
      var(--scene-sky) 0%,
      var(--scene-trees) 28%,
      var(--scene-bank) 48%,
      var(--scene-water) 68%,
      #7f7a72 100%);
  }
  .varietal {
    position: absolute;
    left: 0;
    right: 0;
    top: 820px;
    margin: 0;
    text-align: center;
    font-family: "Pinyon Script", cursive;
    font-weight: 400;
    font-size: 76px;
    line-height: 100px;
    letter-spacing: 22px;
    padding-left: 22px;
    color: var(--varietal);
  }
</style>
</head>
<body>
  <main class="label">
    <h1 class="winery-name">Birchfall Ridge<br>Estate Winery</h1>
    <div class="estate-scene" role="img" aria-label="Photograph of a shallow rocky creek flowing between autumn trees under a pale sky"></div>
    <p class="varietal">Chardonay</p>
  </main>
</body>
</html>
```